Non fiction leadership Book Cover design needed for “Hold Fast: Forge A Steady Track”

I need a front cover design for a new book 6 X 9 traditional non-fiction book.

Title: "Hold FAST - Forge A Steady Track"

The subtitle is not finalized- so use 2 lines of smaller dummy text

My brand guide is attached (please use the tan color sparingly)

I'd like to see FAST look like it is in motion and "flying" across the page

Need CREATIVE designs and options

Do not want my picture on the front cover - I do want it on the back cover.

On the front cover I’d like to see creative use of font to create movement on “FAST”

Target Market(s)

Business leaders

Industry/Entity Type

Aviation

Font styles to use
Other font styles liked:
• See style guide- can add additional font (modern script or san serif)

Colors
0054AA
0677BA
7BADD7
CADEEF
E8F1F8
EB3D1F
EC4F4E
F09395
F8D3D4
FCEDEE

Requirements
Must have
• Creative font use, using perspective to create movement/motion on FAST
Should not have
• My picture on the front cover- my picture should be on the back cover

```html
<!DOCTYPE html>
<html lang="en">
<head>
<meta charset="utf-8">
<title>Hold Fast: Forge A Steady Track — Book Cover</title>
<link rel="stylesheet" href="https://fonts.googleapis.com/css2?family=Bebas+Neue&family=Kaushan+Script&family=Montserrat:wght@600;800&display=swap">
<style>
  :root {
    --page-bg: #eeeeee;
    --navy: #0a1526;
    --deep-blue: #0f2a52;
    --bokeh-blue: #1f4f8f;
    --warm-red: #b3161c;
    --glitter-gold: #c99a4a;
    --white: #ffffff;
    --gold-light: #fff9ec;
    --gold: #f0c46a;
    --gold-deep: #e0a93d;
    --ink: #0b0b0b;
  }
  * { margin: 0; padding: 0; box-sizing: border-box; }
  html, body {
    width: 883px;
    height: 1200px;
    overflow: hidden;
    background: var(--page-bg);
  }
  .cover {
    position: absolute;
    left: 65px;
    top: 35px;
    width: 753px;
    height: 1129px;
    overflow: hidden;
    background: var(--navy);
  }
  .cover-backdrop {
    position: absolute;
    inset: 0;
    background:
      linear-gradient(to top, rgba(201, 154, 74, 0.75) 0%, rgba(201, 154, 74, 0.2) 10%, rgba(201, 154, 74, 0) 20%),
      linear-gradient(to bottom, rgba(179, 22, 28, 0) 30%, rgba(179, 22, 28, 0.55) 55%, rgba(179, 22, 28, 0.6) 80%, rgba(179, 22, 28, 0) 95%),
      linear-gradient(to right, rgba(31, 79, 143, 0) 55%, rgba(31, 79, 143, 0.55) 100%),
      linear-gradient(to bottom, var(--navy) 0%, var(--deep-blue) 100%);
  }
  .book-title { font-weight: normal; }
  .tagline {
    position: absolute;
    top: 46px;
    left: 0;
    width: 100%;
    text-align: center;
    font-family: "Montserrat", sans-serif;
    font-weight: 600;
    font-size: 19px;
    line-height: 25px;
    letter-spacing: 0.3px;
    color: var(--white);
    text-transform: uppercase;
  }
  .title-lead {
    position: absolute;
    top: 352px;
    left: 0;
    width: 100%;
    text-align: center;
    font-family: "Bebas Neue", sans-serif;
    font-size: 172px;
    line-height: 1;
    color: var(--white);
  }
  .title-script {
    position: absolute;
    top: 478px;
    left: 0;
    width: 100%;
    text-align: center;
    font-family: "Kaushan Script", cursive;
    font-size: 236px;
    line-height: 1;
    transform-origin: 30% 50%;
    transform: perspective(700px) rotateY(-24deg) rotate(-9deg) skewX(-10deg);
    filter:
      drop-shadow(5px 4px 0 var(--ink))
      drop-shadow(-18px 6px 0 rgba(240, 196, 106, 0.28))
      drop-shadow(-36px 12px 0 rgba(240, 196, 106, 0.14));
  }
  .title-script span {
    background: linear-gradient(to bottom, var(--gold-light) 10%, var(--gold) 60%, var(--gold-deep) 100%);
    -webkit-background-clip: text;
    background-clip: text;
    color: transparent;
    padding: 0 24px;
  }
  .subtitle {
    position: absolute;
    top: 856px;
    left: 0;
    width: 100%;
    text-align: center;
    font-family: "Montserrat", sans-serif;
    font-weight: 800;
    font-size: 54px;
    line-height: 50px;
    color: var(--white);
    text-transform: uppercase;
  }
  .author {
    position: absolute;
    top: 1010px;
    left: 0;
    width: 100%;
    text-align: center;
    font-family: "Bebas Neue", sans-serif;
    font-size: 86px;
    line-height: 1;
    letter-spacing: 1px;
  }
  .author span {
    background: linear-gradient(to bottom, var(--gold-light) 0%, var(--gold) 55%, var(--gold-deep) 100%);
    -webkit-background-clip: text;
    background-clip: text;
    color: transparent;
  }
</style>
</head>
<body>
  <main class="cover">
    <div class="cover-backdrop" role="img" aria-label="Full-bleed photograph area: dark blue bokeh backdrop with warm red tones through the middle and gold glitter along the bottom"></div>

    <p class="tagline">Lorem ipsum dolor sit amet, consectetur<br>adipiscing elit, sed do eiusmod tempor.</p>

    <h1 class="book-title">
      <span class="title-lead">HOLD</span>
      <span class="title-script"><span>Fast</span></span>
    </h1>

    <p class="subtitle">Forge A<br>Steady Track</p>

    <p class="author"><span>MARIANNE HOLLOWAY</span></p>
  </main>
</body>
</html>
```